Real Estate "For Sale" Sign for construction company

We need a sign that we can use to hang on a post and place on the road when we sell a property. The sign will be simple and will need to mainly feature our logo (files attached), as well as the words "For Sale", and then our phone number "(555) 617 3489". The sign will hang on a post that'll look something like the attached picture.

Target Market(s)

Home buyers

Industry/Entity Type

Real Estate

Font styles to use
Serif
Sans Serif

Colors
0054AA
0677BA
7BADD7
CADEEF
E8F1F8
0094D4
00A9DD
6FCCEA
C7EBF8
E9F6FB

Requirements
Must have
• For Sale & our phone number

```html
<!DOCTYPE html>
<html lang="en">
<head>
<meta charset="utf-8">
<title>For Sale Sign</title>
<link rel="stylesheet" href="https://fonts.googleapis.com/css2?family=Archivo+Black&family=Montserrat:wght@500&display=swap">
<style>
  :root {
    --page-bg: #f3f3f3;
    --sign-white: #ffffff;
    --sign-edge: #8a8a8a;
    --sale-red: #e00000;
    --ink-navy: #142150;
    --rule-blue: #0677BA;
    --brand-blue: #0677BA;
    --brand-dot: #0094D4;
  }
  * { margin: 0; padding: 0; box-sizing: border-box; }
  html, body {
    width: 1200px;
    height: 1200px;
    overflow: hidden;
    background: var(--page-bg);
  }
  .sign {
    position: absolute;
    left: 280px;
    top: 50px;
    width: 640px;
    height: 1100px;
    background: var(--sign-white);
    border: 3px solid var(--sign-edge);
    box-shadow: 0 4px 14px rgba(0,0,0,0.12);
    display: flex;
    flex-direction: column;
    align-items: center;
  }
  .headline-frame {
    margin-top: 55px;
    width: 594px;
    height: 377px;
    border: 3px solid var(--sale-red);
    border-radius: 30px;
    display: flex;
    flex-direction: column;
    align-items: center;
    justify-content: center;
  }
  .headline {
    font-family: "Archivo Black", sans-serif;
    color: var(--sale-red);
    font-size: 172px;
    line-height: 160px;
    text-align: center;
    letter-spacing: 2px;
  }
  .divider {
    margin-top: 45px;
    width: 576px;
    height: 3px;
    background: var(--rule-blue);
  }
  .call-label {
    margin-top: 40px;
    font-family: "Archivo Black", sans-serif;
    color: var(--ink-navy);
    font-size: 42px;
    letter-spacing: 0.5px;
  }
  .phone {
    margin-top: 18px;
    font-family: "Archivo Black", sans-serif;
    color: var(--ink-navy);
    font-size: 112px;
    line-height: 118px;
    text-align: center;
  }
  .brand {
    margin-top: 70px;
    display: flex;
    align-items: center;
    gap: 16px;
  }
  .brand-dot {
    width: 34px;
    height: 34px;
    border-radius: 50%;
    background: var(--brand-dot);
  }
  .brand-name {
    font-family: "Montserrat", sans-serif;
    font-weight: 500;
    color: var(--brand-blue);
    font-size: 46px;
  }
</style>
</head>
<body>
  <main class="sign">
    <div class="headline-frame">
      <h1 class="headline">FOR<br>SALE</h1>
    </div>
    <div class="divider"></div>
    <p class="call-label">CALL OR TEXT US AT:</p>
    <p class="phone">(555)<br>617 3489</p>
    <div class="brand">
      <span class="brand-dot"></span>
      <span class="brand-name">Ridgeline Homes</span>
    </div>
  </main>
</body>
</html>
```